Business Card for premium dental clinic

We are a premium dental clinic based in Brasov, Romania with more than 15 year on the market, providing quality dental treatment made by a team of more specialized dentists, working with modern equipment as a solution to beautiful and healthy teeth.

Our current logo for the clinic use 2 square with colors black and gold - dr Corbescu - studio, using family fonts Bodoni, Myriad Pro and Segoe Print.
Depending on the printing we used some gold CMYK background or gold foil picture background or a gold gradient.
We want a business card:
- eye catching business card
- distinguished business card
- premium design
- to keep the color scheme of black and gold
- to attract the customers to spent time reading the information
- modern concept

```html
<!DOCTYPE html>
<html lang="en">
<head>
<meta charset="utf-8">
<title>dr Corbescu – Business Card</title>
<link href="https://fonts.googleapis.com/css2?family=Montserrat:wght@400;600&display=swap" rel="stylesheet">
<style>
  :root {
    --page: #ffffff;
    --card: #000000;
    --gold: #f2d34f;
    --gold-deep: #d9a92a;
    --ink: #ffffff;
    --shadow: rgba(0, 0, 0, 0.35);
  }
  html, body {
    margin: 0;
    padding: 0;
    width: 1200px;
    height: 900px;
    overflow: hidden;
    background: var(--page);
    font-family: "Montserrat", sans-serif;
  }
  .canvas {
    position: relative;
    width: 1200px;
    height: 900px;
  }
  .card {
    position: absolute;
    left: 261px;
    width: 656px;
    height: 358px;
    background: var(--card);
    box-shadow: 3px 3px 4px var(--shadow);
  }
  .card--front { top: 69px; }
  .card--back { top: 472px; }

  .brand {
    position: absolute;
    display: flex;
    align-items: center;
    gap: 16px;
  }
  .brand__square {
    width: 22px;
    height: 22px;
    background: var(--gold);
    flex: none;
  }
  .brand__name {
    color: var(--gold);
    font-weight: 600;
    white-space: nowrap;
  }
  .card--front .brand {
    left: 37px;
    top: 106px;
    width: 307px;
    height: 146px;
    justify-content: center;
  }
  .card--front .brand__name { font-size: 30px; }
  .card--back .brand {
    left: 193px;
    top: 115px;
    width: 269px;
    height: 128px;
    justify-content: center;
  }
  .card--back .brand__name { font-size: 27px; }

  .divider {
    position: absolute;
    left: 374px;
    top: 106px;
    width: 1.5px;
    height: 146px;
    background: var(--gold);
  }
  .contact {
    position: absolute;
    left: 404px;
    top: 96px;
    color: var(--ink);
  }
  .contact__name {
    margin: 0 0 10px;
    color: var(--gold);
    font-size: 28px;
    font-weight: 600;
    letter-spacing: 1.5px;
    line-height: 1.15;
  }
  .contact__list {
    list-style: none;
    margin: 0;
    padding: 0;
  }
  .contact__item {
    display: flex;
    align-items: center;
    gap: 8px;
    font-size: 16.5px;
    line-height: 21.6px;
    letter-spacing: 0.4px;
  }
  .contact__icon {
    width: 11px;
    height: 11px;
    flex: none;
  }
  .contact__address {
    margin: 8px 0 0;
    font-size: 16.5px;
    line-height: 21.6px;
    letter-spacing: 0.4px;
    font-style: normal;
  }
</style>
</head>
<body>
<main class="canvas">

  <section class="card card--front" aria-label="Business card front">
    <div class="brand">
      <span class="brand__square" aria-hidden="true"></span>
      <span class="brand__name">dr Corbescu</span>
    </div>

    <span class="divider" aria-hidden="true"></span>

    <div class="contact">
      <h1 class="contact__name">DR CORBESCU</h1>
      <ul class="contact__list">
        <li class="contact__item">
          <svg class="contact__icon" viewBox="0 0 12 12" aria-hidden="true">
            <path d="M2.5 1 L4.3 1 L5 3.4 L3.9 4.3 C4.5 5.8 5.8 7.3 7.5 8.1 L8.5 7 L11 7.8 L11 9.6 C11 10.4 10.3 11 9.5 11 C5 10.6 1.3 6.8 1 2.5 C1 1.7 1.7 1 2.5 1 Z" fill="var(--gold)"/>
          </svg>
          <span>+40 268 555 190</span>
        </li>
        <li class="contact__item">
          <svg class="contact__icon" viewBox="0 0 12 12" aria-hidden="true">
            <rect x="0.8" y="2.3" width="10.4" height="7.4" fill="none" stroke="var(--gold)" stroke-width="1.3"/>
            <path d="M1 2.6 L6 6.4 L11 2.6" fill="none" stroke="var(--gold)" stroke-width="1.3"/>
          </svg>
          <span>info@drcorbescu.ro</span>
        </li>
        <li class="contact__item">
          <svg class="contact__icon" viewBox="0 0 12 12" aria-hidden="true">
            <g fill="none" stroke="var(--gold)" stroke-width="1">
              <circle cx="6" cy="6" r="5"/>
              <ellipse cx="6" cy="6" rx="2.2" ry="5"/>
              <path d="M1 6 H11 M1.8 3.4 H10.2 M1.8 8.6 H10.2"/>
            </g>
          </svg>
          <span>www.drcorbescu.ro</span>
        </li>
      </ul>
      <address class="contact__address">Strada Lalelelor 8,<br>Brașov 500100, Romania</address>
    </div>
  </section>

  <section class="card card--back" aria-label="Business card back">
    <div class="brand">
      <span class="brand__square" aria-hidden="true"></span>
      <span class="brand__name">dr Corbescu</span>
    </div>
  </section>

</main>
</body>
</html>
```